new business card design - modern, professional, bold, B2B focus - with QR code pls

we are looking for a modern looking, colorful, business card design. some highlights:
- put space for QR code please. probably on the back but I'm open.
- biz card to be orientated VERTICAL not the traditional horizontal.
- do NOT use our full name on the card (ie: Allied Furnace Servicing Inc). Use only AFS Inc or AFS.
- use black and orange with some white. ideally black card with orange and white for the letters/logo etc. gray ok too - for outlines etc.
- we work in HEAVY industrial, so the cards should lend itself to this. our website is alfurnace.example, so you can see what we do.
- do NOT put in little smoke stack pictures / silouettes etc.
- think MODERN and INDUSTRIAL, with a techy focus.

Industry/Entity Type

heavy industrial - all of them. we perform maintenance and inspection services at heavy industrial and commercial businesses. so B2B

Contact Information for Business Card

name, title, phone numbers (cell + hardline), website, email address. of course our logo too - either on front or front and back.

Font styles to use
Other font styles liked:
• montserrat

Colors
F0912C
F2A743
F7CA91
FBE8D2
FDF5EE

Requirements
Must have
• see description
Nice to have
• see description
Should not have
• see description

```html
<!DOCTYPE html>
<html lang="en">
<head>
<meta charset="utf-8">
<title>AFS Inc – Business Card</title>
<link rel="stylesheet" href="https://fonts.googleapis.com/css2?family=Montserrat:wght@400;600;700&display=swap">
<style>
  :root {
    --backdrop: #dedee4;
    --card: #1b1b1d;
    --orange: #f0912c;
    --orange-soft: #f7ca91;
    --white: #fdf5ee;
    --gray: #5d5d62;
    --shadow: rgba(20, 20, 30, 0.28);
  }
  * { margin: 0; padding: 0; box-sizing: border-box; }
  html, body {
    width: 1200px;
    height: 800px;
    overflow: hidden;
    background: var(--backdrop);
  }
  .canvas {
    width: 1200px;
    height: 800px;
    display: flex;
    align-items: center;
    justify-content: center;
    gap: 96px;
  }
  .card {
    width: 300px;
    height: 525px;
    background: var(--card);
    box-shadow: 0 12px 30px var(--shadow);
    position: relative;
    font-family: "Montserrat", sans-serif;
    color: var(--white);
  }

  /* Front: brand name */
  .card-front {
    display: flex;
    flex-direction: column;
    align-items: center;
    justify-content: center;
  }
  .brand-name {
    font-weight: 700;
    font-size: 72px;
    letter-spacing: 2px;
    color: var(--orange);
    line-height: 1;
  }
  .front-rule {
    width: 64px;
    height: 4px;
    background: var(--orange);
    margin-top: 22px;
  }
  .edge-band {
    position: absolute;
    left: 0;
    right: 0;
    bottom: 0;
    height: 10px;
    background: var(--orange);
  }

  /* Back: contact details */
  .card-back {
    display: flex;
    flex-direction: column;
    align-items: center;
    padding: 52px 24px 0;
  }
  .person-name {
    font-weight: 700;
    font-size: 22px;
    letter-spacing: 0.5px;
    color: var(--orange);
    text-transform: uppercase;
    line-height: 1.2;
  }
  .person-title {
    font-weight: 400;
    font-size: 12px;
    margin-top: 4px;
    color: var(--white);
  }
  .divider {
    width: 40px;
    height: 2px;
    background: var(--gray);
    margin: 22px 0 20px;
  }
  .contact-list {
    list-style: none;
    display: flex;
    flex-direction: column;
    align-items: center;
    gap: 10px;
    font-size: 11px;
    font-weight: 400;
  }
  .contact-item {
    display: flex;
    align-items: center;
    gap: 7px;
    white-space: nowrap;
  }
  .contact-item svg {
    width: 13px;
    height: 13px;
    fill: var(--orange);
    flex: none;
  }
  .qr-space {
    position: absolute;
    left: 50%;
    bottom: 44px;
    width: 104px;
    height: 104px;
    margin-left: -52px;
    border: 2px solid var(--gray);
    background: var(--white);
  }
</style>
</head>
<body>
<main class="canvas">

  <section class="card card-front" aria-label="Card front">
    <span class="brand-name">AFS</span>
    <span class="front-rule"></span>
    <span class="edge-band"></span>
  </section>

  <section class="card card-back" aria-label="Card back">
    <h1 class="person-name">Dana Reyes</h1>
    <p class="person-title">Director</p>
    <span class="divider"></span>

    <ul class="contact-list">
      <li class="contact-item">
        <svg viewBox="0 0 16 16" aria-hidden="true"><path d="M4.5 0h7A1.5 1.5 0 0 1 13 1.5v13a1.5 1.5 0 0 1-1.5 1.5h-7A1.5 1.5 0 0 1 3 14.5v-13A1.5 1.5 0 0 1 4.5 0zm.5 2v10h6V2H5zm3 11a1 1 0 1 0 0 2 1 1 0 0 0 0-2z"/></svg>
        +63 900 555 0147
      </li>
      <li class="contact-item">
        <svg viewBox="0 0 16 16" aria-hidden="true"><path d="M1 3h3v12H1zM5 4h10v11H5zm2 2v2h6V6zm0 4v1.5h1.5V10zm2.5 0v1.5H11V10zM12 10v1.5h1.5V10zM7 12.5V14h1.5v-1.5zm2.5 0V14H11v-1.5zm2.5 0V14h1.5v-1.5z"/></svg>
        +63 900 555 0123
      </li>
      <li class="contact-item">
        <svg viewBox="0 0 16 16" aria-hidden="true"><path d="M0 3h16v10H0zm1.6 1.2L8 9l6.4-4.8z"/></svg>
        info@alfurnace.example
      </li>
      <li class="contact-item">
        <svg viewBox="0 0 16 16" aria-hidden="true"><path d="M8 0a8 8 0 1 0 0 16A8 8 0 0 0 8 0zm0 1.5c.9 0 1.9 1.7 2.3 4H5.7C6.1 3.2 7.1 1.5 8 1.5zM5.5 7h5a13 13 0 0 1 0 2h-5a13 13 0 0 1 0-2zm.2 3.5h4.6c-.4 2.3-1.4 4-2.3 4s-1.9-1.7-2.3-4zM1.6 7h2.4a15 15 0 0 0 0 2H1.6a6.5 6.5 0 0 1 0-2zm10.4 0h2.4a6.5 6.5 0 0 1 0 2H12a15 15 0 0 0 0-2z"/></svg>
        www.alfurnace.example
      </li>
      <li class="contact-item">
        <svg viewBox="0 0 16 16" aria-hidden="true"><path d="M8 0a5.5 5.5 0 0 0-5.5 5.5C2.5 10 8 16 8 16s5.5-6 5.5-10.5A5.5 5.5 0 0 0 8 0zm0 3.2a2.3 2.3 0 1 1 0 4.6 2.3 2.3 0 0 1 0-4.6z"/></svg>
        Dummy Street, Dummy City, Dummy Country
      </li>
    </ul>

    <div class="qr-space" role="img" aria-label="Space reserved for QR code"></div>
  </section>

</main>
</body>
</html>
```